Coffee Shop needs a fresh new menu

Hi,
I would like a new menu to be designed for our coffee shop.
We display our menu on a television screen, so would need it in a file that would allow us to continue to do so -- I have attached a photo so that you can see our current design, and how it is displayed.

I'd like something that is easy to read, if the design could have a "hipster" feel to it -- we are located at a hospital and University.

I have attached a Word file with what we would like on the menu.

Feel free to contact me if you have any questions.

Thanks,
Liv

Just A4 size will be fine, and no need to include menu 1 and menu 2 - I just put them in as an example of what we already have -- they are our printed menu's. Thanks

Hospital

```html
<!DOCTYPE html>
<html lang="en">
<head>
<meta charset="utf-8">
<title>Hot Food and Sandwiches Menu</title>
<link rel="stylesheet" href="https://fonts.googleapis.com/css2?family=Amatic+SC:wght@700&family=Dawning+of+a+New+Day&family=EB+Garamond:ital@1&display=swap">
<style>
  :root {
    --paper: #ece4db;
    --paper-warm: #e8d3c3;
    --splash: #e8467e;
    --panel: rgba(255, 255, 255, 0.82);
    --frame: #eedcd8;
    --card: #fdf8f8;
    --ink: #8c3550;
    --ink-shadow: #f2b9c9;
    --note: #8e4658;
    --band-top: #f1b9ad;
    --band-bottom: #eca39a;
    --bloom: #ee9fc0;
    --bloom-deep: #dc7ea8;
  }
  * { margin: 0; padding: 0; box-sizing: border-box; }
  html, body { width: 847px; height: 1200px; overflow: hidden; }
  body {
    position: relative;
    background:
      radial-gradient(ellipse 200px 120px at 220px 20px, rgba(232, 70, 126, 0.55), transparent 70%),
      radial-gradient(ellipse 160px 260px at 20px 200px, rgba(232, 70, 126, 0.25), transparent 70%),
      radial-gradient(ellipse 300px 500px at 60px 700px, rgba(226, 170, 130, 0.35), transparent 70%),
      linear-gradient(160deg, var(--paper) 0%, var(--paper-warm) 100%);
  }
  .panel {
    position: absolute;
    left: 53px; top: 38px;
    width: 742px; height: 1114px;
    background: var(--panel);
  }
  .menu-frame {
    position: absolute;
    left: 78px; top: 68px;
    width: 695px; height: 669px;
    background: var(--frame);
  }
  .menu-card {
    position: absolute;
    left: 90px; top: 82px;
    width: 670px; height: 640px;
    background:
      radial-gradient(ellipse 220px 160px at 220px 150px, rgba(240, 170, 195, 0.35), transparent 70%),
      var(--card);
  }
  .menu-title {
    position: absolute;
    left: 90px; top: 86px;
    width: 670px;
    text-align: center;
    font-family: "Dawning of a New Day", cursive;
    font-size: 44px;
    line-height: 60px;
    color: var(--ink);
    font-weight: 400;
  }
  .menu-list {
    position: absolute;
    left: 144px; top: 166px;
    width: 564px;
    list-style: none;
  }
  .menu-item {
    display: flex;
    justify-content: space-between;
    height: 48.7px;
    line-height: 48.7px;
    font-family: "Amatic SC", sans-serif;
    font-weight: 700;
    font-size: 42px;
    letter-spacing: 2px;
    color: var(--ink);
    text-shadow: 2px 2px 0 var(--ink-shadow);
  }
  .store-note {
    position: absolute;
    left: 70px; top: 756px;
    width: 708px;
    text-align: center;
    font-family: "EB Garamond", serif;
    font-style: italic;
    font-size: 21px;
    line-height: 28px;
    color: var(--note);
    letter-spacing: 0.3px;
  }
  .color-band {
    position: absolute;
    left: 53px; top: 834px;
    width: 742px; height: 318px;
    background: linear-gradient(180deg, var(--band-top), var(--band-bottom));
  }
  .bloom-art {
    position: absolute;
    left: 262px; top: 850px;
    width: 322px; height: 270px;
    border-radius: 48% 52% 46% 54%;
    background: radial-gradient(circle at 50% 50%, var(--bloom-deep) 0%, var(--bloom) 55%, rgba(238, 159, 192, 0) 100%);
  }
</style>
</head>
<body>
  <div class="panel"></div>
  <div class="menu-frame"></div>
  <div class="menu-card"></div>
  <h1 class="menu-title">-hot food and sandwiches-</h1>
  <ul class="menu-list">
    <li class="menu-item"><span>Pre made sandwiches</span><span>$6.50 - $7.50</span></li>
    <li class="menu-item"><span>Pre made focaccias</span><span>$8.50</span></li>
    <li class="menu-item"><span>Wraps</span><span>$7.50</span></li>
    <li class="menu-item"><span>Vegetarian salad</span><span>$7.50</span></li>
    <li class="menu-item"><span>Meat/seafood salad</span><span>$9.50</span></li>
    <li class="menu-item"><span>Hot chips</span><span>$4.50</span></li>
    <li class="menu-item"><span>Dim sim</span><span>$1.50</span></li>
    <li class="menu-item"><span>Potato cake</span><span>$1.50</span></li>
    <li class="menu-item"><span>Plain hamburger</span><span>$7.50</span></li>
    <li class="menu-item"><span>Hamburger with the lot</span><span>$9.0</span></li>
    <li class="menu-item"><span>Chicken schnitzel burger</span><span>$8.50</span></li>
  </ul>
  <p class="store-note">Our Store inside the Hospital Food Court sells: Hot Pies,<br>Assorted Pasta’s, Ready-to-go Meals, Quiche, and lots more!</p>
  <div class="color-band"></div>
  <div class="bloom-art" role="img" aria-label="Watercolour illustration of a pink rose"></div>
</body>
</html>
```